Discreet simple classy for adult entertainment

I would like a matte black business card with gold writing for my business. Keeping it simple. Having my following:

Lina frost
Events. Entertainment. Promotions
0477250618

or alternatively could have what i had on my previous card below but i think i prefer the above as again - discretion.

Maybe a nice gold line thru the card or some other very simple design . Or not open to ideas/ can be doublesided if any good ideas with that.

included pics of my old bus card. not sure weather i want a photo on it or not. if i do it wont be the same pic. i kinda wanted a card that was discreet so if it was in someones wallet they wouldn't neccessarily realise it was from a stripper.

Target Market(s)

men

Industry/Entity Type

Business

Contact Information for Business Card

Lina frost
0477250618

Requirements
Nice to have
• i don't know i am really open to anything. im giving my cards to guys so something they can have in their wallet that is discreet preferably.

```html
<!DOCTYPE html>
<html lang="en">
<head>
<meta charset="utf-8">
<title>Lina Frost – Business Card</title>
<link rel="stylesheet" href="https://fonts.googleapis.com/css2?family=Montserrat:wght@400;700&family=Josefin+Sans:wght@300;400&display=swap">
<style>
  :root {
    --stage: #e9e6e1;
    --card-black: #0b0d14;
    --card-navy: #151a28;
    --gold-deep: #b07f22;
    --gold-light: #f2cc66;
    --photo-top: #2c3a4a;
    --photo-mid: #a97f63;
    --photo-low: #f0d6c7;
    --chip-black: #0a0a0a;
    --chip-text: #ffffff;
  }
  * { box-sizing: border-box; margin: 0; padding: 0; }
  html, body { width: 1200px; height: 950px; overflow: hidden; }
  body {
    background: var(--stage);
    display: flex;
    align-items: center;
    justify-content: center;
    gap: 60px;
  }
  .card { box-shadow: 0 14px 34px rgba(0,0,0,.28); position: relative; overflow: hidden; }
  .card-front {
    width: 560px; height: 320px;
    background: linear-gradient(100deg, var(--card-black) 0%, var(--card-navy) 35%, var(--card-black) 55%, var(--card-navy) 78%, var(--card-black) 100%);
    display: flex; flex-direction: column; align-items: center; justify-content: center;
    color: var(--gold-light);
  }
  .gold {
    background: linear-gradient(90deg, var(--gold-deep), var(--gold-light) 50%, var(--gold-deep));
    -webkit-background-clip: text; background-clip: text; color: transparent;
  }
  .name {
    font-family: "Montserrat", sans-serif; font-weight: 700;
    font-size: 44px; letter-spacing: 5px; text-transform: uppercase;
  }
  .tagline {
    font-family: "Josefin Sans", sans-serif; font-weight: 400;
    font-size: 13px; letter-spacing: 1.5px; text-transform: uppercase;
    margin-top: 6px;
  }
  .rule {
    width: 150px; height: 1px; margin: 18px 0;
    background: linear-gradient(90deg, transparent, var(--gold-light), transparent);
  }
  .phone {
    font-family: "Josefin Sans", sans-serif; font-weight: 300;
    font-size: 38px; letter-spacing: 3px;
  }
  .card-back { width: 320px; height: 560px; }
  .portrait {
    position: absolute; inset: 0;
    background: linear-gradient(170deg, var(--photo-top) 0%, var(--photo-mid) 45%, var(--photo-low) 100%);
  }
  .social {
    position: absolute; right: 22px; bottom: 26px;
    display: flex; align-items: center; gap: 8px;
    font-family: "Montserrat", sans-serif; font-weight: 700; font-size: 13px;
    color: var(--chip-black);
  }
  .social-dot { width: 22px; height: 22px; border-radius: 50%; background: var(--chip-black); }
</style>
</head>
<body>
  <section class="card card-front">
    <div class="rule"></div>
    <h1 class="name gold">Lina Frost</h1>
    <p class="tagline gold">Events. Entertainment. Promotions</p>
    <div class="rule"></div>
    <p class="phone gold">0477250618</p>
  </section>
  <section class="card card-back">
    <div class="portrait" role="img" aria-label="Portrait photograph of the card owner"></div>
    <div class="social"><span class="social-dot"></span><span>linafrost</span></div>
  </section>
</body>
</html>
```